Specialised investor in e-mobility and energy wants business card design

We need a business card design that fits our existing corporate design. <The look and feel must be 'sharp'/'clean', dynamic, communicate momentum, professionalism etc (as one would imagine from a firm in the financial sector). We like the idea of a reverse-side of the card that includes the logo, and the name and contact details on the other. We expect the deliverable to be whatever format might be required to be able to get cards printed directly by a service such as tandor press. Our website is www.orm.capital

```html
<!DOCTYPE html>
<html lang="en">
<head>
<meta charset="utf-8">
<title>ORM Capital – Business Card</title>
<link href="https://fonts.googleapis.com/css2?family=Montserrat:wght@400;500;700&display=swap" rel="stylesheet">
<style>
  :root {
    --backdrop: #cdd1d0;
    --paper: #f4f4f2;
    --green-dark: #1d4a14;
    --green-mid: #2f6a1c;
    --green-light: #6fae34;
    --ink: #2b2b2b;
    --ghost: #e2e3df;
  }
  * { margin: 0; padding: 0; box-sizing: border-box; }
  html, body { width: 1200px; height: 905px; overflow: hidden; }
  body {
    background: var(--backdrop);
    font-family: "Montserrat", sans-serif;
    position: relative;
  }
  .card {
    position: absolute;
    top: 290px;
    width: 540px;
    height: 309px;
    background: var(--paper);
    overflow: hidden;
    box-shadow: 0 12px 30px rgba(0,0,0,.18);
  }
  .card--front { left: 40px; }
  .card--back { left: 620px; }

  .ghost-name {
    position: absolute;
    font-weight: 700;
    color: var(--ghost);
    white-space: nowrap;
    letter-spacing: 2px;
  }
  .card--front .ghost-name { left: 60px; top: 2px; font-size: 84px; }
  .card--back .ghost-name { right: -10px; bottom: -22px; font-size: 120px; }

  .person { position: absolute; left: 34px; top: 48px; }
  .person__name {
    font-weight: 700;
    font-size: 21px;
    letter-spacing: .5px;
    color: var(--green-dark);
  }
  .person__name span { color: var(--green-light); }
  .person__role { font-size: 12px; color: var(--ink); margin-top: 2px; }

  .divider {
    position: absolute;
    left: 34px; right: 40px; top: 116px;
    height: 1px;
    background: var(--green-dark);
  }

  .contacts { position: absolute; left: 34px; top: 134px; list-style: none; }
  .contacts li {
    display: flex; align-items: center; gap: 8px;
    font-size: 12px; color: var(--ink); margin-bottom: 7px;
  }
  .contacts svg { width: 11px; height: 11px; fill: var(--green-light); }

  .wordmark {
    position: absolute;
    display: flex; align-items: center; gap: 10px;
    font-weight: 500;
    color: var(--green-dark);
    white-space: nowrap;
  }
  .wordmark__dot { border-radius: 50%; background: var(--green-light); }
  .card--front .wordmark { right: 40px; top: 44px; font-size: 30px; }
  .card--front .wordmark__dot { width: 14px; height: 14px; }
  .card--back .wordmark { left: 50%; top: 50%; transform: translate(-50%, -60%); font-size: 46px; }
  .card--back .wordmark__dot { width: 20px; height: 20px; }

  .address {
    position: absolute; right: 40px; bottom: 40px;
    font-size: 12px; line-height: 1.45; color: var(--ink); text-align: right;
  }
  .band { position: absolute; left: 0; bottom: 0; width: 100%; height: 14px; }
</style>
</head>
<body>

<section class="card card--front" aria-label="Card front">
  <div class="ghost-name" aria-hidden="true">ORM</div>
  <div class="person">
    <h1 class="person__name">MARCUS <span>REVELL</span></h1>
    <p class="person__role">Director/Founder</p>
  </div>
  <div class="wordmark"><span class="wordmark__dot"></span>ORM Capital</div>
  <div class="divider"></div>
  <ul class="contacts">
    <li><svg viewBox="0 0 24 24"><path d="M6.6 10.8a15 15 0 0 0 6.6 6.6l2.2-2.2a1 1 0 0 1 1-.25 11 11 0 0 0 3.6.6 1 1 0 0 1 1 1V20a1 1 0 0 1-1 1A17 17 0 0 1 3 4a1 1 0 0 1 1-1h3.5a1 1 0 0 1 1 1 11 11 0 0 0 .6 3.6 1 1 0 0 1-.25 1z"/></svg>123-480-2917</li>
    <li><svg viewBox="0 0 24 24"><path d="M2 5h20v2l-10 6L2 7zm0 4 10 6 10-6v10H2z"/></svg>info@orm.capital</li>
    <li><svg viewBox="0 0 24 24"><circle cx="12" cy="12" r="10"/></svg>www.orm.capital</li>
  </ul>
  <p class="address">88 Harbour Lane<br>Northvale CD 3120</p>
  <svg class="band" viewBox="0 0 540 14" preserveAspectRatio="none" aria-hidden="true">
    <polygon points="0,0 200,0 215,14 0,14" fill="var(--green-mid)"/>
    <polygon points="200,0 540,0 540,14 215,14" fill="var(--green-light)"/>
  </svg>
</section>

<section class="card card--back" aria-label="Card back">
  <div class="ghost-name" aria-hidden="true">ORM</div>
  <div class="wordmark"><span class="wordmark__dot"></span>ORM Capital</div>
</section>

</body>
</html>
```